Bytemill - a software development company requires letter head

I currently have a business card and logo, I just need a nice looking letter head the matches the two. I will upload these Illustrator files.

I would like the letter head to be done in a current version of MS Word.

Please incorporate 'bytemill' as per the attached font and the logo.

Industry/Entity Type

Computer Software

Colors

Designer to choose colors to be used in the design.

Requirements
Must have
• Fits in with current design, sleek and professional. It will be used for quotations and tenders and documentation going to clients and potential clients.
• Would like to company logo up the top header and perhaps a watermark of the logo at the bottom right, a bit like the business card.
• Also it needs to be MS word.
• Please work with the color pallet from the attached files.

```html
<!DOCTYPE html>
<html lang="en">
<head>
<meta charset="utf-8">
<title>Bytemill Letterhead</title>
<link href="https://fonts.googleapis.com/css2?family=Roboto:wght@400;500&display=swap" rel="stylesheet">
<style>
  :root {
    --backdrop: #e8e8e8;
    --paper: #f7f7f7;
    --brand-blue: #2a9fd8;
    --watermark: #dbe8ee;
    --text-grey: #6e6e6e;
    --text-dark: #4a4a4a;
  }
  * { margin: 0; padding: 0; box-sizing: border-box; }
  html, body {
    width: 1200px; height: 866px; overflow: hidden;
    background: var(--backdrop);
    font-family: "Roboto", sans-serif;
  }
  .letterhead {
    position: absolute; left: 300px; top: 13px;
    width: 600px; height: 840px;
    background: var(--paper);
    overflow: hidden;
    color: var(--text-grey);
  }
  .brand {
    position: absolute; left: 53px; top: 92px;
    display: flex; align-items: center; gap: 10px;
  }
  .brand-dot { width: 16px; height: 16px; border-radius: 50%; background: var(--brand-blue); }
  .brand-name {
    font-size: 30px; font-weight: 500; letter-spacing: 1px;
    color: var(--brand-blue); text-transform: uppercase;
  }
  .contact {
    position: absolute; right: 50px; top: 82px;
    list-style: none; text-align: right;
    font-size: 9.5px; line-height: 14px; color: var(--text-dark);
  }
  .contact li { display: flex; justify-content: flex-end; align-items: flex-start; gap: 6px; }
  .contact li + li { margin-top: 2px; }
  .contact .icon { width: 10px; height: 10px; margin-top: 2px; flex: none; }
  .contact .spacer { width: 10px; flex: none; }
  .accent-bar {
    position: absolute; right: 1px; top: 79px;
    width: 14px; height: 63px; background: var(--brand-blue);
  }
  .recipient {
    position: absolute; left: 53px; top: 228px;
    font-size: 11px; line-height: 15.7px;
  }
  .body-copy {
    position: absolute; left: 53px; top: 321px; width: 496px;
    font-size: 10.6px; line-height: 15.5px; text-align: justify;
  }
  .body-copy p + p { margin-top: 31px; }
  .signature {
    position: absolute; left: 52px; top: 556px;
    width: 114px; height: 72px;
    background: linear-gradient(120deg, rgba(42,159,216,0.18), rgba(42,159,216,0.06));
    border-radius: 4px;
  }
  .sign-title {
    position: absolute; left: 52px; top: 644px;
    font-size: 10.8px;
  }
  .watermark {
    position: absolute; left: 346px; top: 644px;
    width: 252px; height: 252px; border-radius: 50%;
    background: var(--watermark);
  }
</style>
</head>
<body>
  <main class="letterhead">
    <div class="brand">
      <span class="brand-dot"></span>
      <span class="brand-name">Bytemill</span>
    </div>

    <ul class="contact">
      <li>+61 400 12 3987
        <svg class="icon" viewBox="0 0 10 10" aria-hidden="true"><circle cx="5" cy="5" r="5" fill="#2a9fd8"/><path d="M3.2 2.6c.4-.3.8 0 1 .5l.2.5c.1.3-.2.5-.3.7.3.6.8 1.1 1.4 1.4.2-.1.4-.4.7-.3l.5.2c.5.2.8.6.5 1-.5.6-1.3.7-2.2.1C4 6 3.4 5.3 3 4.5c-.4-.8-.3-1.5.2-1.9z" fill="#fff"/></svg>
      </li>
      <li>PO Box 218
        <svg class="icon" viewBox="0 0 10 10" aria-hidden="true"><circle cx="5" cy="5" r="5" fill="#2a9fd8"/><path d="M5 2.2a1.8 1.8 0 0 1 1.8 1.8C6.8 5.3 5 7.8 5 7.8S3.2 5.3 3.2 4A1.8 1.8 0 0 1 5 2.2z" fill="#fff"/><circle cx="5" cy="4" r=".7" fill="#2a9fd8"/></svg>
      </li>
      <li style="margin-top:0">Rosewood SA 5061<span class="spacer"></span></li>
      <li>tom@bytemill.co
        <svg class="icon" viewBox="0 0 10 10" aria-hidden="true"><circle cx="5" cy="5" r="5" fill="#2a9fd8"/><rect x="2.6" y="3.3" width="4.8" height="3.4" rx=".4" fill="#fff"/><path d="M2.8 3.5 5 5.2l2.2-1.7" stroke="#2a9fd8" stroke-width=".5" fill="none"/></svg>
      </li>
    </ul>
    <div class="accent-bar"></div>

    <address class="recipient" style="font-style:normal">
      Dear Harrowby<br>
      Lantern Print Works Ltd<br>
      Department Design
    </address>

    <section class="body-copy">
      <p>Lorem ipsum dolor sit amet, consectetuer adipiscing elit. Aenean commodo ligula eget dolor. Aenean massa. Cum sociis natoque penatibus et magnis dis parturient montes, nascetur ridiculus mus. Donec quam felis, ultricies nec, pellentesque eu, pretium quis, sem. Nulla consequat massa quis enim. Donec pede justo, fringilla vel, aliquet nec, vulputate eget, arcu. In enim justo, rhoncus ut, imperdiet a, venenatis vitae, justo. Nullam dictum felis eu pede mollis pretium. Integer tincidunt. Cras dapibus. Vivamus elementum semper nisi.Nullam dictum felis eu pede mollis pretium. Integer tincidunt. Cras dapibus. Vivamus elementum semper nisi.felis eu pede mollis pretium. Integer tincidunt. Cras dapibus.</p>
      <p>Quisque rutrum. Aenean imperdiet. Etiam ultricies nisi vel augue. Curabitur ullamcorper ultricies nisi. Nam eget dui. Etiam rhoncus. Maecenas tempus, tellus eget condimentum rhoncus, sem quam semper libero, sit amet adipiscing sem neque sed ipsum.felis pede mollis pretium. I am tincidunt. Cras dapibus.</p>
    </section>

    <div class="signature" role="img" aria-label="Handwritten signature of the director in blue ink"></div>
    <p class="sign-title">Director/Excecutive Director</p>

    <div class="watermark" aria-hidden="true"></div>
  </main>
</body>
</html>
```